Entertainment Sound and Lighting company Business card

We need a professional looking business card designed for my growing entertainment sound and lighting company based in Sydney, Australia called "Kestrel Sound"

We provide technical production services (sound systems/lighting/vision) for events ranging from band gigs, weddings, corporate functions etc.

The business card needs to contain the following information:

Bartholomew Quenneville
Audio Engineer
Phone: 0478 615 702
Email: bartholomew@kestrelsound.com.au
Website: www.kestrelsound.com.au

Business logo has been attached in .ai format, please contact me if you need me to provide other files.

Target Market(s)

We need a business card that reflects our modern and professional company but still looks professional to appeal to our corporate clients.
We have a very broad target market spanning from bands needing PA systems for their gigs (18-30yrs) to event companies needing sound and lighting for weddings and other functions.

Industry/Entity Type

Business

Requirements
Must have
• Needs to include the logo that is attached of course, and the colour scheme.
Nice to have
• - Double sided

```html
<!DOCTYPE html>
<html lang="en">
<head>
<meta charset="utf-8">
<title>Kestrel Sound – Business Card</title>
<link href="https://fonts.googleapis.com/css2?family=Arimo:wght@400;700&display=swap" rel="stylesheet">
<style>
  :root {
    --stage: #8e8e8e;
    --stage-top: #5a5a5a;
    --card-white: #ffffff;
    --card-black: #050505;
    --brand-blue: #1b7fc1;
    --brand-cyan: #23b6e8;
    --ink: #111111;
    --spot: #5c5c5c;
  }
  html, body {
    margin: 0;
    padding: 0;
    overflow: hidden;
  }
  .canvas {
    position: relative;
    width: 1200px;
    height: 900px;
    background: linear-gradient(180deg, var(--stage-top) 0%, var(--stage) 60%, #d6d6d6 100%);
    font-family: "Arimo", Arial, sans-serif;
    overflow: hidden;
  }

  /* Front: landscape black card */
  .card-front {
    position: absolute;
    left: 130px;
    top: 290px;
    width: 560px;
    height: 320px;
    background: var(--card-black);
    box-shadow: 0 10px 30px rgba(0,0,0,0.35);
    overflow: hidden;
  }
  .card-front .stage-art {
    position: absolute;
    inset: 0;
    background:
      radial-gradient(ellipse 60% 12% at 50% 86%, rgba(230,230,230,0.55) 0%, rgba(230,230,230,0) 100%),
      linear-gradient(180deg, var(--spot) 0%, #2a2a2a 55%, var(--card-black) 100%);
    clip-path: polygon(28% 0, 72% 0, 92% 100%, 8% 100%);
  }
  .card-front .wordmark {
    position: absolute;
    left: 0;
    right: 0;
    top: 205px;
    text-align: center;
    font-size: 52px;
    font-weight: 700;
    color: var(--brand-blue);
    letter-spacing: -1px;
  }

  /* Back: portrait white card */
  .card-back {
    position: absolute;
    left: 750px;
    top: 170px;
    width: 320px;
    height: 560px;
    background: var(--card-white);
    box-shadow: 0 10px 30px rgba(0,0,0,0.35);
    text-align: center;
    overflow: hidden;
  }
  .card-back .wordmark {
    margin-top: 92px;
    font-size: 30px;
    font-weight: 700;
    color: var(--brand-blue);
    letter-spacing: -0.5px;
  }
  .card-back .identity {
    margin-top: 72px;
  }
  .card-back .person-name {
    font-size: 16px;
    color: var(--brand-blue);
    margin: 0;
  }
  .card-back .person-role {
    font-size: 11px;
    font-weight: 700;
    color: var(--ink);
    margin: 3px 0 0;
  }
  .card-back .contacts {
    margin: 22px 0 0;
    padding: 0;
    list-style: none;
    font-size: 13.5px;
    color: var(--ink);
  }
  .card-back .contacts li {
    margin-bottom: 4px;
    line-height: 1.15;
  }
  .card-back .contacts .label {
    display: block;
    color: var(--brand-cyan);
    font-size: 13px;
  }
  .card-back .sound-band {
    position: absolute;
    left: 20px;
    right: 20px;
    bottom: 30px;
    height: 130px;
    background: linear-gradient(180deg, rgba(35,182,232,0.85) 0%, rgba(27,127,193,0.35) 70%, rgba(255,255,255,0) 100%);
  }
</style>
</head>
<body>
<main class="canvas">
  <section class="card-front">
    <div class="stage-art" role="img" aria-label="Spotlit stage with speaker stack and headphones"></div>
    <div class="wordmark">Kestrel Sound</div>
  </section>

  <section class="card-back">
    <div class="wordmark">Kestrel Sound</div>
    <div class="identity">
      <p class="person-name">Bartholomew Quenneville</p>
      <p class="person-role">Audio Engineer</p>
    </div>
    <ul class="contacts">
      <li><span class="label">t</span>0478 615 702</li>
      <li><span class="label">e</span>bartholomew@kestrelsound.com.au</li>
      <li><span class="label">w</span>www.kestrelsound.com.au</li>
    </ul>
    <div class="sound-band" role="img" aria-label="Blue sound wave decoration"></div>
  </section>
</main>
</body>
</html>
```